Kestrel Plumbing business card full re design & logo design

Kestrel Plumbing is a Sydney based mechanical plumbing contractor company.
We would like a full redesign with new logo etc which we can take to a future website, uniforms, vehicle sign writing etc.
Blue is my preferred choice of colour but i would be open to see a couple of alternatives thrown in the mix to see how they compare. I am open to see on white cards, black cards etc. Open to many new ideas.
Please see attached original business cards which have been used for the last 5 years.

Target Market(s)

Mechanical services industry.

Industry/Entity Type

Plumbing

Contact Information for Business Card

Dale Fenmore
Director

Mob: 0427 596 418
Email: dale@kestrelplumbing-demo.net.au
PO BOX 782
Harbourvale NSW 2199
Lic: 518604k

Logo Text

Kestrel Plumbing

Font styles to use
Sans Serif

Colors
0655a3
3276b5
0792cd
33a6d7
85cae6
000000
333333
474747

Requirements
Must have
• Things that make it very professional and very well presented.
Nice to have
• Same description or very similar to attached uploaded file
Should not have
• Anything that makes it look unprofessional or cartoony.

```html
<!DOCTYPE html>
<html lang="en">
<head>
<meta charset="utf-8">
<title>Kestrel Plumbing – Business Card</title>
<link rel="stylesheet" href="https://fonts.googleapis.com/css2?family=Montserrat:wght@400;500;600;700&family=Roboto:wght@300;400;500&display=swap">
<style>
  :root {
    --brand-blue: #0655a3;
    --accent-blue: #3276b5;
    --bright-blue: #0792cd;
    --ink: #333333;
    --ink-soft: #474747;
    --paper: #ffffff;
    --backdrop: #3a3a3c;
  }
  * { box-sizing: border-box; margin: 0; padding: 0; }
  html, body {
    width: 1200px; height: 810px; overflow: hidden;
    background: var(--backdrop);
  }
  .canvas {
    position: relative; width: 1200px; height: 810px;
    display: flex; align-items: center; justify-content: center; gap: 40px;
  }
  .card {
    position: relative; width: 540px; height: 330px; overflow: hidden;
    box-shadow: 0 12px 30px rgba(0,0,0,.45);
  }

  /* Back of card */
  .card--back { background: var(--brand-blue); color: var(--paper); font-family: "Montserrat", sans-serif; }
  .services-title {
    position: absolute; left: 34px; top: 30px;
    font-size: 20px; font-weight: 600; letter-spacing: 1.5px;
  }
  .services-intro {
    position: absolute; left: 44px; top: 76px;
    font-size: 18px; font-weight: 600; letter-spacing: .5px;
  }
  .services-list {
    position: absolute; left: 50px; top: 110px; list-style: none;
    font-size: 15px; font-weight: 500; line-height: 25px; letter-spacing: .6px;
  }
  .services-list li::before {
    content: ""; display: inline-block; width: 6px; height: 6px; border-radius: 50%;
    background: var(--paper); margin: 0 12px 2px 0; vertical-align: middle;
  }
  .tagline {
    position: absolute; left: 46px; bottom: 26px;
    font-family: "Roboto", sans-serif; font-size: 14px; font-weight: 500; font-style: italic;
  }
  .brand {
    position: absolute; display: flex; align-items: center; gap: 14px;
    font-family: "Montserrat", sans-serif; font-weight: 700;
  }
  .brand__mark { width: 44px; height: 44px; border-radius: 50%; flex: none; }
  .brand__name { line-height: 1.05; letter-spacing: 1px; }
  .brand__name span { display: block; }
  .card--back .brand { right: 36px; top: 128px; color: var(--paper); font-size: 26px; }
  .card--back .brand__mark { background: var(--paper); }

  /* Front of card */
  .card--front { background: var(--paper); font-family: "Montserrat", sans-serif; color: var(--ink); }
  .card--front .brand { left: 34px; top: 48px; color: var(--accent-blue); font-size: 26px; }
  .card--front .brand__mark { background: var(--accent-blue); }
  .holder { position: absolute; right: 34px; top: 48px; text-align: right; }
  .holder__name { font-size: 24px; font-weight: 600; color: var(--accent-blue); letter-spacing: 1px; }
  .holder__role { font-family: "Roboto", sans-serif; font-size: 14px; color: var(--ink-soft); margin-top: 2px; }
  .rule { position: absolute; left: 34px; right: 34px; top: 158px; height: 1.5px; background: var(--accent-blue); }
  .contact {
    position: absolute; left: 34px; bottom: 40px;
    font-family: "Roboto", sans-serif; font-size: 14px; line-height: 22px; color: var(--ink-soft);
  }
  .contact b, .address b { font-weight: 500; color: var(--ink); }
  .address {
    position: absolute; right: 34px; top: 186px; text-align: right;
    font-family: "Roboto", sans-serif; font-size: 14px; line-height: 20px; color: var(--ink-soft);
  }
  .corner-band { position: absolute; right: 0; bottom: 0; }
</style>
</head>
<body>
<main class="canvas">

  <section class="card card--back">
    <h2 class="services-title">MECHANICAL PLUMBING SERVICES</h2>
    <p class="services-intro">Specialising in:</p>
    <ul class="services-list">
      <li>Make Good</li>
      <li>Refurbishment</li>
      <li>Tenancy Fit Out</li>
      <li>Plant Room Works</li>
      <li>Shut Downs</li>
      <li>Change Overs</li>
    </ul>
    <p class="tagline">KESTREL have the SOLUTION</p>
    <div class="brand">
      <span class="brand__mark"></span>
      <p class="brand__name"><span>KESTREL</span><span>PLUMBING</span></p>
    </div>
  </section>

  <section class="card card--front">
    <div class="brand">
      <span class="brand__mark"></span>
      <p class="brand__name"><span>KESTREL</span><span>PLUMBING</span></p>
    </div>
    <div class="holder">
      <p class="holder__name">Dale Fenmore</p>
      <p class="holder__role">Director</p>
    </div>
    <div class="rule"></div>
    <div class="address">
      <p><b>Address:</b> P. O. Box 782</p>
      <p>Harbourvale NSW 2199</p>
    </div>
    <div class="contact">
      <p><b>Mobile:</b> 0427 596 418</p>
      <p><b>Email:</b> dale@kestrelplumbing-demo.net.au</p>
      <p><b>Lic:</b> 518604k</p>
    </div>
    <svg class="corner-band" width="200" height="14" viewBox="0 0 200 14" aria-hidden="true">
      <polygon points="10,0 200,0 200,14 0,14" fill="var(--accent-blue)"/>
    </svg>
  </section>

</main>
</body>
</html>
```